Banner ads for do-it-yourself website maker

We need banner ads for a FREE do-it-yourself website maker.

Our website is: http://www.brimlake.com

We are seeking TEN different 720x90 banner ads that convince people to try the product.

The ads should be simple single-image jpgs, although they also could be animated GIFs if the size can be kept down (under 150k)

To see what we offer, check out the website - or, a quick summary follows:

- Free, No need to give credit card, etc
- Do it yourself website builder
- All inclusive (hosting, cloud-based tools)
- One-time fee if want to add your own URL
- Mobile website support
- Easy to use, but powerful enough for PROS
- Websites, or powerful blogging
- Blogging features (blog by email, or via webpage), rss feeds, social media integration
- Full SEO support
- Low-cost option to pay if you want to skill the ads
- Widget-based system (Photo galleries, blog, comment, store, ecommerce, subscription payments, message boards, contact forms)
- Powerful newsletter feature
- Security (integrated user management, lock down the whole site, or individual pages)
Updates

I notice that the first design that came in was five "spins" on one creative idea. At the other end of this process my goal is to come out with ten completely different banners, NOT one idea in ten different designs.

The design that was submitted was excellent and had some great ideas in it.. so, the process does seem to be working. I'm very curious to see everyone's good ideas!

-Dale R

I should also mention...

The ads will be cycled through (on different days/times) when run - so, no one ad has to tell the whole story. My thought is that each ad tells a part of the story (the ads do have to work on their own), but that when combined, with the target audience seeing them over a period of weeks, they get the full message of why our product is great.

Target Market(s)

Our target audience are serious bloggers seeking to make money on their blog. Also small business people (photographers, plumbers, accountants, web designers).

Industry/Entity Type

Credit Card

Colors

Designer to choose colors to be used in the design.

Requirements
Must have
• Grab the person quickly - something that cuts through the clutter. Examples:

"Need a website?
Your website can be live 15 minutes from now!
FREE - why not try now?"

Or ..

"Serious bloggers need serious power. One of our bloggers just surpassed 200,000 readers. Are you ready for action?"

Or ...

"Tired of waiting on a geek to do your website?
Why wait. We have hundreds of professionally designed templates.
Get started now. Do it yourself. Free."

Or...

??? All ideas appreciated.
Nice to have
• Send a message of simple - but, not so simple that we are competing with the simplistic products - We are do it yourself for people who are willing to invest some effort to create something they won't outgrow. If they are looking for a simple one-page website - that is really just an online yellow-pages listing - we may not be right for them. We are do-it-yourself for people who appreciate power, and are willing to do some work to have a free site.

```html
<!DOCTYPE html>
<html lang="en">
<head>
<meta charset="utf-8">
<title>Brimlake banner ads</title>
<link rel="stylesheet" href="https://fonts.googleapis.com/css2?family=Source+Sans+3:wght@400;600;700;800&family=Barlow+Condensed:wght@600;700&display=swap">
<style>
:root{
  --backdrop:#2b2b2c;
  --navy:#0b3468;
  --navy-deep:#072650;
  --navy-shade:#06204a;
  --sky:#1a7cc4;
  --ink:#ffffff;
  --gold:#ffc81f;
  --yellow:#ffe11a;
  --btn-top:#2a95de;
  --btn-bottom:#0f5fae;
  --orange-top:#ffb12a;
  --orange-bottom:#f07800;
  --slate:#3e4a66;
  --paper:#ffffff;
}
*{box-sizing:border-box;margin:0;padding:0}
html,body{width:1200px;height:1029px;overflow:hidden;background:var(--backdrop)}
body{font-family:"Source Sans 3",sans-serif;color:var(--ink)}
.stage{position:relative;width:1220px;height:1046px;transform:scale(0.98361);transform-origin:0 0}
.banner{position:absolute;left:231px;width:720px;height:90px;overflow:hidden;background:var(--navy)}
.abs{position:absolute}
.brand{position:absolute;display:flex;align-items:center;gap:8px;font-weight:700;font-size:25px;letter-spacing:.5px;color:var(--ink);white-space:nowrap}
.brand-square{width:14px;height:14px;background:var(--ink)}
.btn{position:absolute;display:flex;align-items:center;justify-content:center;font-weight:600;font-size:15px;color:var(--ink);border-radius:2px;
  background:linear-gradient(var(--btn-top),var(--btn-bottom));box-shadow:0 2px 3px rgba(0,0,0,.45)}
.btn-orange{background:linear-gradient(var(--orange-top),var(--orange-bottom));font-size:16px;font-weight:400}
.shade{position:absolute;right:0;bottom:0;width:130px;height:90px;background:var(--navy-shade);clip-path:polygon(0 40%,100% 40%,100% 100%,55% 100%)}
.imagery{position:absolute}
.check{display:flex;align-items:center;gap:5px;font-size:10px;line-height:11px}
.ribbon{position:absolute;left:0;top:0;width:90px;height:90px;border-right:1px dashed rgba(255,255,255,.7)}
.ribbon-line{position:absolute;left:0;bottom:8px;width:90px;height:14px;border-top:1px dashed rgba(255,255,255,.7)}
.caption{position:absolute;left:0;width:1185px;top:940px;text-align:center;font-size:31px;color:#eee}
</style>
</head>
<body>
<main class="stage">

  <section class="banner" style="top:36px">
    <div class="brand" style="left:14px;top:28px"><span class="brand-square"></span>BRIMLAKE</div>
    <p class="abs" style="left:230px;top:9px;width:350px;text-align:center;font-size:15.5px;line-height:21px">Serious bloggers need serious power. One of our bloggers just surpassed <b>200,000 readers.</b></p>
    <p class="abs" style="left:230px;top:54px;width:350px;text-align:center;font-size:21px;font-weight:700">Are you ready <span style="color:var(--gold)">for action?</span></p>
    <div class="shade"></div>
    <div class="btn" style="left:598px;top:29px;width:105px;height:33px">Get Started</div>
  </section>

  <section class="banner" style="top:139px;background:linear-gradient(90deg,#0d4d92,var(--sky) 55%,#0f5aa3)">
    <div class="abs" style="left:0;top:0;width:102px;height:90px;background:#0c4785;border-right:1px solid #3b8fd2"></div>
    <div class="abs" style="left:14px;top:35px;font-weight:700;font-size:17px;letter-spacing:.5px">BRIMLAKE</div>
    <div class="abs" style="left:140px;top:13px;width:355px;height:56px;background:rgba(8,38,80,.55)"></div>
    <p class="abs" style="left:146px;top:15px;font-size:21px">Serious bloggers need serious power.</p>
    <p class="abs" style="left:146px;top:46px;font-size:16px">One of our bloggers just surpassed 200,000 readers.</p>
    <p class="abs" style="right:11px;top:14px;font-size:15px"><b>Are you ready</b> for action?</p>
    <div class="btn" style="left:578px;top:46px;width:104px;height:32px">Get Started</div>
  </section>

  <section class="banner" style="top:243px">
    <div class="brand" style="left:10px;top:35px;font-size:15px;gap:6px"><span class="brand-square" style="width:9px;height:9px"></span>BRIMLAKE</div>
    <p class="abs" style="left:113px;top:21px;font-size:20px;line-height:25px"><b>Need a website?</b> Your website<br>can be live <b>15 minutes</b> from now!</p>
    <div class="abs" style="left:414px;top:8px;display:flex;flex-direction:column;gap:5px">
      <div class="check"><svg width="22" height="22" viewBox="0 0 22 22"><circle cx="11" cy="11" r="10" fill="#fff"/><path d="M6 11l3.5 3.5L16 7.5" stroke="#0b3468" stroke-width="2.6" fill="none"/></svg><span><b>FREE</b> to Use</span></div>
      <div class="check"><svg width="22" height="22" viewBox="0 0 22 22"><circle cx="11" cy="11" r="10" fill="#fff"/><path d="M6 11l3.5 3.5L16 7.5" stroke="#0b3468" stroke-width="2.6" fill="none"/></svg><span><b>ONLINE</b> in minutes</span></div>
      <div class="check"><svg width="22" height="22" viewBox="0 0 22 22"><circle cx="11" cy="11" r="10" fill="#fff"/><path d="M6 11l3.5 3.5L16 7.5" stroke="#0b3468" stroke-width="2.6" fill="none"/></svg><span>No Experience Required</span></div>
    </div>
    <svg class="abs" style="left:568px;top:0" width="152" height="90" viewBox="0 0 152 90"><path d="M14 0 Q-6 45 14 90 H152 V0Z" fill="#5aa3e0"/><path d="M18 0 Q-2 45 18 90 H152 V0Z" fill="#fff"/></svg>
    <p class="abs" style="left:594px;top:21px;font-size:10.5px;color:#333"><b style="color:#111">FREE</b> - why not try now?</p>
    <div class="btn" style="left:601px;top:45px;width:106px;height:33px">Get Started</div>
  </section>

  <section class="banner" style="top:346px;background:var(--slate)">
    <div class="ribbon" style="background:var(--navy)"></div><div class="ribbon-line"></div>
    <div class="abs" style="left:10px;top:34px;font-weight:700;font-size:14px">BRIMLAKE</div>
    <p class="abs" style="left:104px;top:9px;font-size:18px;font-weight:700;color:var(--yellow)">Create <span style="font-weight:400">a</span> professional website!</p>
    <p class="abs" style="left:100px;top:36px;width:245px;text-align:center;font-size:13px;line-height:16px"><b>Serious bloggers</b> need <b>serious power.</b><br>One of our bloggers just surpassed<br><b>200,000 readers!</b></p>
    <div class="imagery" role="img" aria-label="Row of website template screenshots" style="left:353px;top:6px;width:214px;height:78px;background:linear-gradient(90deg,#e8e2d6,#c9b79a 50%,#e3d9c7)"></div>
    <p class="abs" style="left:580px;top:7px;width:124px;text-align:center;font-size:14.5px;font-weight:600">Are you ready?</p>
    <svg class="abs" style="left:634px;top:28px" width="12" height="14" viewBox="0 0 12 14"><path d="M1 1l5 5 5-5M1 7l5 5 5-5" stroke="#ccc" stroke-width="1.8" fill="none"/></svg>
    <div class="btn btn-orange" style="left:580px;top:48px;width:124px;height:32px">Get Started</div>
  </section>

  <section class="banner" style="top:451px">
    <div class="ribbon"></div><div class="ribbon-line"></div>
    <div class="abs" style="left:10px;top:34px;font-weight:700;font-size:14px">BRIMLAKE</div>
    <p class="abs" style="left:104px;top:9px;font-size:18px;font-weight:700;color:var(--yellow)">Create <span style="font-weight:400">a</span> professional website!</p>
    <p class="abs" style="left:100px;top:36px;width:245px;text-align:center;font-size:13px;line-height:16px"><b>Serious bloggers</b> need <b>serious power.</b><br>One of our bloggers just surpassed<br><b>200,000 readers!</b></p>
    <div class="imagery" role="img" aria-label="Row of website template screenshots" style="left:353px;top:6px;width:214px;height:78px;background:linear-gradient(90deg,#e8e2d6,#c9b79a 50%,#e3d9c7)"></div>
    <p class="abs" style="left:580px;top:7px;width:124px;text-align:center;font-size:14.5px;font-weight:600">Are you ready?</p>
    <svg class="abs" style="left:634px;top:28px" width="12" height="14" viewBox="0 0 12 14"><path d="M1 1l5 5 5-5M1 7l5 5 5-5" stroke="#ccc" stroke-width="1.8" fill="none"/></svg>
    <div class="btn btn-orange" style="left:580px;top:48px;width:124px;height:32px">Get Started</div>
  </section>

  <section class="banner" style="top:557px;background:#05080f">
    <div class="ribbon" style="left:8px;width:80px;background:var(--navy-deep)"></div>
    <div class="abs" style="left:8px;bottom:8px;width:80px;height:14px;border-top:1px dashed rgba(255,255,255,.7)"></div>
    <div class="abs" style="left:16px;top:36px;font-weight:700;font-size:13px">BRIMLAKE</div>
    <p class="abs" style="left:105px;top:7px;font-size:16.5px">Tired of waiting on a geek to do your <b>website?</b></p>
    <p class="abs" style="left:105px;top:29px;font-size:12px">Why wait. We have <b>100s</b> of professionally designed templates.</p>
    <p class="abs" style="left:105px;top:52px;font-family:'Barlow Condensed',sans-serif;font-weight:700;font-size:24px">Get started now. Do it yourself. FREE.</p>
    <div class="imagery" role="img" aria-label="Website template preview with business photo" style="left:458px;top:0;width:130px;height:90px;clip-path:polygon(12% 0,100% 0,88% 100%,0 100%);background:linear-gradient(135deg,#2f8fc0,#9fd3ea 55%,#3c6f8e)"></div>
    <p class="abs" style="left:595px;top:13px;font-size:19px">Try it <b>FREE!</b></p>
    <div class="btn btn-orange" style="left:580px;top:46px;width:124px;height:32px">Get Started</div>
  </section>

  <section class="banner" style="top:663px">
    <div class="brand" style="left:14px;top:28px"><span class="brand-square"></span>BRIMLAKE</div>
    <p class="abs" style="left:240px;top:14px;font-size:19px">Create a <b>Professional Website</b> for FREE!</p>
    <div class="abs" style="left:260px;top:50px;display:flex;gap:18px">
      <div class="check"><svg width="30" height="30" viewBox="0 0 22 22"><circle cx="11" cy="11" r="10" fill="#fff"/><path d="M6 11l3.5 3.5L16 7.5" stroke="#0b3468" stroke-width="2.6" fill="none"/></svg><span style="text-align:center">FREE<br>to Use</span></div>
      <div class="check"><svg width="30" height="30" viewBox="0 0 22 22"><circle cx="11" cy="11" r="10" fill="#fff"/><path d="M6 11l3.5 3.5L16 7.5" stroke="#0b3468" stroke-width="2.6" fill="none"/></svg><span>Online in<br>Minutes</span></div>
      <div class="check"><svg width="30" height="30" viewBox="0 0 22 22"><circle cx="11" cy="11" r="10" fill="#fff"/><path d="M6 11l3.5 3.5L16 7.5" stroke="#0b3468" stroke-width="2.6" fill="none"/></svg><span>No Experience<br>Required</span></div>
    </div>
    <div class="shade"></div>
    <div class="btn" style="left:598px;top:29px;width:105px;height:33px">Get Started</div>
  </section>

  <section class="banner" style="top:767px">
    <svg class="abs" style="left:0;top:0" width="92" height="90" viewBox="0 0 92 90"><path d="M0 0H80 Q98 45 80 90H0Z" fill="var(--paper)"/></svg>
    <div class="abs" style="left:8px;top:36px;font-weight:700;font-size:14px;color:var(--navy)">BRIMLAKE</div>
    <div class="imagery" role="img" aria-label="Row of website template screenshots" style="left:110px;top:6px;width:215px;height:78px;background:linear-gradient(90deg,#e8e2d6,#c9b79a 50%,#e3d9c7)"></div>
    <p class="abs" style="left:340px;top:12px;width:240px;text-align:center;font-size:15.5px;line-height:21px"><b>Serious bloggers</b> need <b>serious power.</b> One of our bloggers just surpassed <b>200,000 readers!</b></p>
    <p class="abs" style="left:598px;top:10px;width:105px;text-align:center;font-size:13px;line-height:13px">Are you ready<br><b>for action?</b></p>
    <div class="btn" style="left:598px;top:47px;width:105px;height:32px">Get Started</div>
  </section>

  <p class="caption">Gif banner: Link in description</p>
</main>
</body>
</html>
```